User-interface and web design for new forum-style communication platform

We developed a new forum-style communication platform specially targetting stock investors to share and discuss information on companies listed on the stock exchange.

You have complete freedom for designing the user-interface and web design. Designs should include all features listed below.

Please read the attached document for full specifications. Also attached is a mockup of the layout, but this is only directional. A mockup for the user-profile is also attached, but does not need to be designed.

This project focusses on the homepage and thread view.

The winner(s) will be asked to design the complete project. (create thread box, user profile, registering, settings...)

We are looking for a well thought out, smart design that incorporates the specifications in the attached document. Please do not hesitate to contact us if anything is not clear.

Target Market(s)

Stock investors from 25 to 60 years old (the people that are currently on investor forums)

Industry/Entity Type

Communication

Font styles to use
Sans Serif

Colors

Designer to choose colors to be used in the design.

Requirements
Must have
• Full homepage design & Thread view specified in the attached document.
Nice to have
• Create thread view
- Field for adding tags
- field for subject of the thread
- text box with basic text editing
- method for sharing media
Should not have
• Logo design.

```html
<!DOCTYPE html>
<html lang="en">
<head>
<meta charset="UTF-8">
<title>Vestora – Public Conversations</title>
<link rel="stylesheet" href="https://fonts.googleapis.com/css2?family=Open+Sans:wght@400;600;700&family=Montserrat:wght@700&display=swap">
<style>
  :root {
    --blue: #0b83cf;
    --blue-bright: #1b9be3;
    --pill: #2eaeee;
    --ink: #222;
    --text: #555;
    --muted: #888;
    --line: #e1e1e1;
    --panel-border: #d6d6d6;
    --dark: #3a3a3a;
    --footer: #333;
    --page: #ffffff;
    --header-top: #ffffff;
    --header-bottom: #eeeeee;
    --avatar-bg: #e9e9e9;
    --avatar-fg: #ffffff;
    --badge: #e62323;
  }
  * { box-sizing: border-box; margin: 0; padding: 0; }
  html, body { width: 1200px; height: 1103px; overflow: hidden; }
  body {
    position: relative;
    background: var(--page);
    font-family: "Open Sans", Arial, sans-serif;
    color: var(--text);
    font-size: 12px;
  }
  .abs { position: absolute; }

  /* Header */
  .site-header {
    position: absolute; left: 0; top: 0; width: 1200px; height: 84px;
    background: linear-gradient(var(--header-top), var(--header-bottom));
    border-bottom: 1px solid #dcdcdc;
  }
  .brand {
    position: absolute; left: 160px; top: 27px;
    font-weight: 700; font-size: 25px; letter-spacing: 0.5px; color: var(--blue);
  }
  .top-search {
    position: absolute; left: 442px; top: 29px; width: 429px; height: 32px;
    border: 2px solid #d4d4d4; border-radius: 4px; background: #fff;
    display: flex; align-items: center; overflow: hidden;
  }
  .top-search svg { margin: 0 12px 0 10px; }
  .top-search .query { flex: 1; font-size: 14px; color: #777; }
  .top-search .btn-dark {
    height: 28px; width: 59px; background: var(--dark); color: #fff;
    font-size: 14px; display: flex; align-items: center; justify-content: center;
    border-left: 1px solid #555;
  }
  .notify {
    position: absolute; left: 891px; top: 31px; width: 37px; height: 28px;
    background: #8fcdf2; border-radius: 2px; display: flex; align-items: center; justify-content: center;
  }
  .notify .badge {
    position: absolute; right: -7px; bottom: -5px; width: 15px; height: 14px;
    background: var(--badge); color: #fff; border-radius: 3px;
    font-size: 10px; font-weight: 700; text-align: center; line-height: 14px;
  }
  .user-select {
    position: absolute; left: 946px; top: 29px; width: 94px; height: 33px;
    border: 1px solid #d4d4d4; background: #fff;
    display: flex; align-items: center; font-size: 12px; color: #777;
  }
  .user-select span { flex: 1; padding-left: 10px; }
  .user-select .caret {
    width: 21px; height: 100%; background: var(--blue-bright);
    display: flex; align-items: center; justify-content: center;
  }

  /* Sidebar */
  .user-card {
    position: absolute; left: 160px; top: 115px; width: 196px; height: 85px;
    background: linear-gradient(#4c4c4c, #2e2e2e); border-radius: 2px;
  }
  .user-card .name {
    position: absolute; left: 10px; top: 10px; display: flex; align-items: center;
    color: #fff; font-size: 14px; font-weight: 600; gap: 9px;
  }
  .user-card .side-search {
    position: absolute; left: 9px; top: 46px; width: 178px; height: 29px;
    background: #fff; border-radius: 3px; display: flex; align-items: center;
    padding-left: 13px; font-style: italic; color: #555; font-size: 12px;
  }
  .user-card .side-search .go {
    position: absolute; right: 4px; top: 3px; width: 23px; height: 23px;
    border-radius: 50%; background: #2d2d2d; display: flex; align-items: center; justify-content: center;
  }
  .side-panel {
    position: absolute; left: 160px; width: 196px; height: 248px;
    border: 1px solid var(--panel-border); background: #fff;
  }
  .side-panel .panel-head {
    height: 27px; margin: -1px -1px 0; background: linear-gradient(var(--blue-bright), #0a86d2);
    color: #fff; font-size: 14px; font-weight: 600; padding-left: 9px; line-height: 27px; position: relative;
  }
  .side-panel .toggle {
    position: absolute; right: 8px; top: 6px; width: 14px; height: 14px;
    background: #fff; border-radius: 50%;
  }
  .side-panel .toggle::after {
    content: ""; position: absolute; left: 4px; top: 6px; width: 6px; height: 2px; background: var(--blue);
  }
  .side-panel ul { list-style: none; }
  .side-panel li {
    height: 28px; line-height: 28px; padding-left: 9px;
    border-bottom: 1px solid #ececec; font-size: 12px; color: #666;
  }
  .side-panel .view-all {
    display: flex; align-items: center; gap: 6px; padding: 12px 0 0 15px;
    color: var(--blue); font-size: 12px; font-weight: 600;
  }

  /* Main column */
  .breadcrumb {
    position: absolute; left: 385px; top: 115px; width: 655px; height: 26px;
    border: 1px solid var(--line); padding-left: 8px; line-height: 24px; font-size: 11.5px; color: #333;
  }
  .breadcrumb a { color: var(--blue); text-decoration: none; }
  .breadcrumb .sep { color: #999; margin: 0 3px; }
  .tabs {
    position: absolute; left: 385px; top: 161px; width: 655px; height: 39px;
    border: 1px solid #dcdcdc; background: linear-gradient(#fafafa, #ececec);
    display: flex; align-items: stretch; border-radius: 2px;
  }
  .tabs .tab {
    padding: 0 17px; line-height: 37px; font-size: 15px; color: #666;
    border-right: 1px solid #dcdcdc; position: relative;
  }
  .tabs .tab.active { color: var(--blue); background: #fff; }
  .tabs .tab.active::after {
    content: ""; position: absolute; left: 50%; bottom: -1px; margin-left: -7px;
    border: 7px solid transparent; border-bottom-color: #dcdcdc; border-top: 0;
  }
  .tabs .create {
    margin-left: auto; align-self: center; margin-right: 9px;
    background: #3c3c3c; color: #fff; border-radius: 12px; padding: 3px 7px;
    font-size: 12.5px;
  }

  .post {
    position: absolute; left: 385px; width: 655px; height: 184px;
    border: 1px solid var(--line); border-radius: 2px; background: #fff;
  }
  .avatar {
    position: absolute; background: var(--avatar-bg); overflow: hidden;
  }
  .post .avatar { left: 19px; top: 19px; width: 65px; height: 65px; }
  .post .subject {
    position: absolute; left: 101px; top: 17px;
    font-family: "Montserrat", Arial, sans-serif; font-weight: 700; font-size: 15px; color: var(--ink);
  }
  .post .meta { position: absolute; left: 101px; top: 43px; font-size: 11.5px; color: var(--muted); }
  .post .meta b { font-weight: 400; color: #333; }
  .post .meta .bar { margin: 0 8px; }
  .post .body {
    position: absolute; left: 101px; top: 70px; width: 530px;
    font-size: 12.2px; line-height: 19px; color: #666;
  }
  .post .actions {
    position: absolute; left: 101px; top: 140px; display: flex; align-items: center;
    font-size: 11.5px; color: #333; gap: 4px;
  }
  .post .actions .stat { margin-left: 16px; display: flex; align-items: center; gap: 5px; }
  .post .pills { position: absolute; right: 28px; top: 139px; display: flex; gap: 10px; }
  .pill {
    width: 66px; height: 21px; border-radius: 11px; background: var(--pill);
    color: #fff; font-size: 12px; text-align: center; line-height: 21px;
  }

  .reply-avatar { left: 385px; top: 439px; width: 44px; height: 44px; }
  .reply-box {
    position: absolute; left: 449px; top: 439px; width: 591px; height: 66px;
    border: 1px solid var(--line); padding: 8px 10px; font-size: 12px; color: #777;
  }
  .send { position: absolute; left: 459px; top: 515px; }
  .attach { position: absolute; left: 968px; top: 515px; display: flex; gap: 8px; }

  .site-footer {
    position: absolute; left: 0; top: 1062px; width: 1200px; height: 41px;
    background: var(--footer); color: #eee; font-size: 12.5px; text-align: center; line-height: 41px;
  }
</style>
</head>
<body>

<header class="site-header">
  <div class="brand">VESTORA</div>
  <div class="top-search">
    <svg width="15" height="15" viewBox="0 0 15 15"><circle cx="9" cy="6" r="4.5" fill="none" stroke="#999" stroke-width="1.4"/><line x1="5.8" y1="9.2" x2="1.5" y2="13.5" stroke="#999" stroke-width="1.6"/></svg>
    <span class="query"># northwind #lumora</span>
    <span class="btn-dark">Save</span>
    <span class="btn-dark">Clear</span>
  </div>
  <div class="notify">
    <svg width="20" height="14" viewBox="0 0 20 14"><circle cx="7" cy="4" r="3.2" fill="#1668a8"/><path d="M1 13c0-4 3-5.5 6-5.5s6 1.5 6 5.5z" fill="#1668a8"/><circle cx="13.5" cy="4" r="2.8" fill="#1668a8"/><path d="M12 7.6c3 0 7 1 7 5.4h-4.5c0-2.5-1-4-2.5-5.4z" fill="#1668a8"/></svg>
    <span class="badge">3</span>
  </div>
  <div class="user-select">
    <span>User</span>
    <div class="caret"><svg width="9" height="6" viewBox="0 0 9 6"><path d="M0 0h9L4.5 6z" fill="#fff"/></svg></div>
  </div>
</header>

<aside>
  <div class="user-card">
    <div class="name">
      <svg width="22" height="22" viewBox="0 0 22 22"><circle cx="11" cy="11" r="10" fill="none" stroke="#fff" stroke-width="1.6"/><circle cx="11" cy="8.5" r="3.4" fill="#fff"/><path d="M4.8 17.5c1.2-3 3.6-4.3 6.2-4.3s5 1.3 6.2 4.3a9 9 0 0 1-12.4 0z" fill="#fff"/></svg>
      User
    </div>
    <div class="side-search">Search
      <span class="go"><svg width="12" height="12" viewBox="0 0 12 12"><circle cx="5" cy="5" r="3.6" fill="none" stroke="#fff" stroke-width="1.5"/><line x1="7.6" y1="7.6" x2="11" y2="11" stroke="#fff" stroke-width="1.6"/></svg></span>
    </div>
  </div>

  <section class="side-panel" style="top:228px">
    <div class="panel-head">Save Filters<span class="toggle"></span></div>
    <ul><li>Item One</li><li>Item Two</li><li>Item Three</li><li>Item Four</li><li>Item Five</li><li>Item Six</li></ul>
    <div class="view-all">View All <svg width="11" height="11" viewBox="0 0 11 11"><circle cx="5.5" cy="5.5" r="5.5" fill="#222"/><path d="M3 5.5h4.5M5.5 3.3l2.2 2.2-2.2 2.2" stroke="#fff" stroke-width="1.3" fill="none"/></svg></div>
  </section>

  <section class="side-panel" style="top:505px">
    <div class="panel-head">Popular Tags<span class="toggle"></span></div>
    <ul><li>Item One</li><li>Item Two</li><li>Item Three</li><li>Item Four</li><li>Item Five</li><li>Item Six</li></ul>
    <div class="view-all">View All <svg width="11" height="11" viewBox="0 0 11 11"><circle cx="5.5" cy="5.5" r="5.5" fill="#222"/><path d="M3 5.5h4.5M5.5 3.3l2.2 2.2-2.2 2.2" stroke="#fff" stroke-width="1.3" fill="none"/></svg></div>
  </section>

  <section class="side-panel" style="top:782px">
    <div class="panel-head">Popular Contributors<span class="toggle"></span></div>
    <ul><li>Item One</li><li>Item Two</li><li>Item Three</li><li>Item Four</li><li>Item Five</li><li>Item Six</li></ul>
    <div class="view-all">View All <svg width="11" height="11" viewBox="0 0 11 11"><circle cx="5.5" cy="5.5" r="5.5" fill="#222"/><path d="M3 5.5h4.5M5.5 3.3l2.2 2.2-2.2 2.2" stroke="#fff" stroke-width="1.3" fill="none"/></svg></div>
  </section>
</aside>

<main>
  <nav class="breadcrumb">
    <a>Home</a><span class="sep">&gt;</span><a>Conversation</a><span class="sep">&gt;</span><a>Public</a><span class="sep">&gt;</span># northwind #lumora
  </nav>

  <div class="tabs">
    <div class="tab active">Public</div>
    <div class="tab">Following</div>
    <div class="tab" style="border-right:0">Contacts</div>
    <div class="create">Create thread</div>
  </div>

  <article class="post" style="top:226px">
    <div class="avatar" role="img" aria-label="Author profile picture placeholder"></div>
    <h2 class="subject">LOREM IPSUM SUBJECT</h2>
    <div class="meta"><b>By:</b> Martin Hale<span class="bar">|</span>Jan 01, 2014<span class="bar">|</span>15:32</div>
    <p class="body">Lorem Ipsum is simply dummy text of the printing and typesetting industry. Lorem Ipsum has been the industry standard dummy text ever since 1500s, when an unknown printer .</p>
    <div class="actions">[ Read more ]
      <span class="stat">12 <svg width="9" height="8" viewBox="0 0 9 8"><path d="M8 0v4H2M4 2 2 4l2 2" stroke="#bbb" fill="none" stroke-width="1.2"/></svg></span>
      <span class="stat">250 <svg width="13" height="8" viewBox="0 0 13 8"><path d="M.5 4C3 0 10 0 12.5 4 10 8 3 8 .5 4z" fill="none" stroke="#bbb"/><circle cx="6.5" cy="4" r="1.8" fill="#bbb"/></svg></span>
    </div>
    <div class="pills"><span class="pill">reply</span><span class="pill">share</span><span class="pill">favourite</span></div>
  </article>

  <div class="avatar reply-avatar" role="img" aria-label="Your profile picture placeholder"></div>
  <div class="reply-box">Type your reply here...</div>
  <span class="pill send">send</span>
  <div class="attach">
    <svg width="13" height="14" viewBox="0 0 13 14"><path d="M1.5.5h7l3 3v10h-10z" fill="none" stroke="#999"/><path d="M4 10c2-3 3-5 2.5-6S5 5 7 8s2 2 2 2" fill="none" stroke="#999" stroke-width=".8"/></svg>
    <svg width="14" height="14" viewBox="0 0 14 14"><rect x=".5" y=".5" width="13" height="13" fill="none" stroke="#999"/><path d="M3.5.5v13M10.5.5v13M.5 5h3M.5 9h3M10.5 5h3M10.5 9h3" stroke="#999"/></svg>
    <svg width="16" height="14" viewBox="0 0 16 14"><path d="M1 3.5h3.5L6 1.5h4l1.5 2H15V13H1z" fill="#999"/><circle cx="8" cy="8" r="3" fill="#fff"/><circle cx="8" cy="8" r="1.8" fill="#999"/></svg>
  </div>

  <article class="post" style="top:564px">
    <div class="avatar" role="img" aria-label="Author profile picture placeholder"></div>
    <h2 class="subject">LOREM IPSUM SUBJECT</h2>
    <div class="meta"><b>By:</b> Martin Hale<span class="bar">|</span>Jan 01, 2014<span class="bar">|</span>15:32</div>
    <p class="body">Lorem Ipsum is simply dummy text of the printing and typesetting industry. Lorem Ipsum has been the industry standard dummy text ever since 1500s, when an unknown printer .</p>
    <div class="actions">[ Read more ]
      <span class="stat">12 <svg width="9" height="8" viewBox="0 0 9 8"><path d="M8 0v4H2M4 2 2 4l2 2" stroke="#bbb" fill="none" stroke-width="1.2"/></svg></span>
      <span class="stat">250 <svg width="13" height="8" viewBox="0 0 13 8"><path d="M.5 4C3 0 10 0 12.5 4 10 8 3 8 .5 4z" fill="none" stroke="#bbb"/><circle cx="6.5" cy="4" r="1.8" fill="#bbb"/></svg></span>
    </div>
    <div class="pills"><span class="pill">reply</span><span class="pill">share</span><span class="pill">favourite</span></div>
  </article>

  <article class="post" style="top:774px">
    <div class="avatar" role="img" aria-label="Author profile picture placeholder"></div>
    <h2 class="subject">LOREM IPSUM SUBJECT</h2>
    <div class="meta"><b>By:</b> Martin Hale<span class="bar">|</span>Jan 01, 2014<span class="bar">|</span>15:32</div>
    <p class="body">Lorem Ipsum is simply dummy text of the printing and typesetting industry. Lorem Ipsum has been the industry standard dummy text ever since 1500s, when an unknown printer .</p>
    <div class="actions">[ Read more ]
      <span class="stat">12 <svg width="9" height="8" viewBox="0 0 9 8"><path d="M8 0v4H2M4 2 2 4l2 2" stroke="#bbb" fill="none" stroke-width="1.2"/></svg></span>
      <span class="stat">250 <svg width="13" height="8" viewBox="0 0 13 8"><path d="M.5 4C3 0 10 0 12.5 4 10 8 3 8 .5 4z" fill="none" stroke="#bbb"/><circle cx="6.5" cy="4" r="1.8" fill="#bbb"/></svg></span>
    </div>
    <div class="pills"><span class="pill">reply</span><span class="pill">share</span><span class="pill">favourite</span></div>
  </article>
</main>

<footer class="site-footer">© Copyrights 2014 Vestora. All Rights Reserved</footer>

</body>
</html>
```